intraoral tooth cleaning device requires JAZZY NEW PACKAGING

I already have a logo design for my product "GLIMMO" but I need a sharply designed packaging. Something that is bright and stands out.
Glimmo is an anatomically and ergonomically correct dental plaque remover. It
"Makes Every Smile Brightly Fresh".
Go to my website myglimmo.example to get the logo design and the look and feel of the product. Also there is more information about the product.
I am trying to get a package with 10 pieces of Glimmo in each package. I also would be interested in packaging for 20 pieces also..I would like the package to be like a pack of cigarettes and fit in a shirt pocket.
Colors used should be green, white, yellow, blue. Clean pharmaceutical looking.
The Glimmo is easy to use, only one hand required and it is reusable.
On you tube I have 2 videos listed under "glimmo hd" Watch them for more info.
I am sending more variations of the "GLIMMO" logo that I have designed. They are very good variations.
Updates

Reason: Only have 5 responses. I thought there was to be at least 50.????

I am very sorry that I have not given any feed back. But there is a very good reason. I ALMOST DIED 4 TIMES.I was vomiting food on every meal and went through many tests to find the problem. It was determined that I had a diverticulum of the esophagus, or a bubble that if it had burst I would have died very quickly. I had a surgery on Feb 13, 2014 that was meant to fix this condition, But did not turn out very well for me. I have had 4 more surgeries since. I am doing much better now and I hope this last surgery will fix the problem. I again would like to apologize to all of the designers that submitted a design. Truly there was not much I could have done, I was fighting for my life. I would like to extend the date by an extra month from now if that is okay with all of the designers. You all have done a great job. And now that I have most of my energy back I can devote some time to completing this project. Most Respectfully Yours Dr. Martin L. Hobbes

Target Market(s)

Anyone with teeth that gets food stuck in between them. Mostly adults , not really children, though I have my own kids who love them.

Industry/Entity Type

Dental

Requirements
Must have
• Clean, Healthy look and feel. A look that promotes health and well being.
• something pharmaceutical like. Clean colors blue,green, white, yellow.
Nice to have
• the advantages of Dr. designed, non-abrasive to tooth structure. Easy to use. Re-usable. Safe for dental implants.
Should not have
• old design, dark colors, i.e. browns, grays, nothing drab.

```html
<!DOCTYPE html>
<html lang="en">
<head>
<meta charset="utf-8">
<title>Glimmo Package Design</title>
<link href="https://fonts.googleapis.com/css2?family=PT+Sans:wght@400;700&family=PT+Sans+Narrow:wght@400;700&display=swap" rel="stylesheet">
<style>
  :root {
    --bg: #eceef0;
    --white: #ffffff;
    --blue: #1d5fa6;
    --navy: #173f7a;
    --teal: #2a8fb0;
    --green: #1e6b34;
    --green-light: #3c9a50;
    --yellow: #f4d21f;
    --line: #5b7fb8;
    --text: #2e3f5c;
  }
  * { box-sizing: border-box; margin: 0; padding: 0; }
  html, body { width: 1200px; height: 900px; overflow: hidden; }
  body {
    background: var(--bg);
    font-family: "PT Sans", sans-serif;
    color: var(--text);
    position: relative;
  }
  .dieline {
    position: absolute;
    left: 130px; top: 200px;
    display: flex;
    box-shadow: 0 6px 24px rgba(0,0,0,.12);
  }
  .panel {
    position: relative;
    height: 500px;
    background: var(--white);
    overflow: hidden;
    border-right: 1px dashed #c9d1dc;
  }
  .panel:last-child { border-right: none; }
  .panel--side { width: 130px; }
  .panel--face { width: 340px; }

  .wordmark {
    position: absolute;
    font-family: "PT Sans", sans-serif;
    font-weight: 700;
    color: var(--blue);
    line-height: 1;
    white-space: nowrap;
  }
  .wordmark__dot {
    display: inline-block;
    width: .28em; height: .28em;
    border-radius: 50%;
    background: var(--green-light);
    margin-left: .12em;
    vertical-align: .55em;
  }
  .tagline {
    position: absolute;
    font-family: "PT Sans Narrow", sans-serif;
    font-weight: 700;
    color: var(--green);
    white-space: nowrap;
  }

  .band { position: absolute; left: 0; bottom: 0; width: 100%; height: 110px; }

  /* front */
  .front .wordmark { left: 26px; top: 44px; font-size: 50px; }
  .front .tagline { left: 28px; top: 100px; font-size: 14px; }
  .wave-art {
    position: absolute; left: 0; top: 140px; width: 230px; height: 165px;
    background: linear-gradient(160deg, rgba(255,255,255,0) 10%, #cfe3d4 45%, #a9cdb3 60%, rgba(255,255,255,0) 90%);
  }
  .product-art {
    position: absolute; left: 272px; top: 60px; width: 52px; height: 280px;
    background: linear-gradient(90deg, #f4f6f8, #dfe5ea 50%, #f4f6f8);
    border-radius: 26px 26px 22px 22px;
  }
  .claim {
    position: absolute; left: 22px; top: 318px;
    font-family: "PT Sans Narrow", sans-serif;
    font-size: 15px; color: var(--blue);
    white-space: nowrap;
  }
  .product-name {
    position: absolute; left: 22px; top: 336px;
    font-weight: 700; font-size: 22px; color: var(--navy);
    white-space: nowrap;
  }
  .count-badge {
    position: absolute; left: 272px; top: 352px; width: 46px; height: 74px;
    background: var(--green); color: var(--white);
    border-radius: 6px; text-align: center;
    font-family: "PT Sans Narrow", sans-serif; font-weight: 700;
    padding-top: 5px;
  }
  .count-badge__label { font-size: 10px; display: block; }
  .count-badge__num { font-size: 28px; line-height: 1; display: block; border: 2px solid var(--white); margin: 3px 4px; border-radius: 3px; }
  .count-badge__unit { font-size: 10px; display: block; }
  .seal { position: absolute; left: 14px; top: 385px; width: 110px; height: 100px; }
  .features {
    position: absolute; left: 148px; top: 428px; list-style: none;
    font-family: "PT Sans Narrow", sans-serif; font-weight: 700;
    font-size: 13px; color: var(--yellow); letter-spacing: .3px;
  }
  .features li { margin-bottom: 4px; display: flex; align-items: center; gap: 7px; }
  .features li::before {
    content: ""; width: 0; height: 0;
    border-left: 7px solid var(--yellow);
    border-top: 5px solid transparent; border-bottom: 5px solid transparent;
  }

  /* left side */
  .side-left .wordmark { left: 14px; top: 22px; font-size: 24px; }
  .side-left .tagline { left: 14px; top: 50px; font-size: 7px; }
  .info-box {
    position: absolute; border: 1px solid var(--line); border-radius: 4px;
    padding: 8px; font-size: 9px; line-height: 1.35; color: var(--text);
  }
  .info-box h3 { font-size: 11px; color: var(--navy); margin-bottom: 4px; }
  .info-box p { margin-bottom: 8px; }
  .side-left .info-box { left: 10px; top: 95px; width: 110px; height: 140px; }
  .batch { position: absolute; left: 10px; top: 270px; width: 110px; }
  .batch__row { display: flex; align-items: center; margin-bottom: 6px; font-size: 9px; font-weight: 700; color: var(--navy); }
  .batch__row span { width: 40px; }
  .batch__field { flex: 1; height: 18px; border: 1px solid var(--line); }

  /* back */
  .back .wordmark { left: 100px; top: 50px; font-size: 44px; }
  .back .tagline { left: 92px; top: 100px; font-size: 12px; }
  .back .info-box { left: 14px; top: 130px; width: 312px; height: 150px; font-size: 8.5px; }

  /* right side */
  .side-right .wordmark { left: 14px; top: 30px; font-size: 24px; }
  .side-right .tagline { left: 14px; top: 58px; font-size: 7px; }
  .side-right .info-box { left: 8px; top: 95px; width: 114px; height: 260px; }
  .diagram {
    position: absolute; left: 40px; top: 30px; width: 28px; height: 210px;
    background: linear-gradient(90deg, #eef1f4, #d8dfe6, #eef1f4);
    border-radius: 14px;
  }
  .diagram-label { position: absolute; font-size: 7.5px; line-height: 1.15; color: var(--text); }
  .marks { position: absolute; left: 14px; bottom: 18px; display: flex; gap: 6px; }
  .marks span { width: 16px; height: 16px; border-radius: 50%; background: var(--white); opacity: .9; }
</style>
</head>
<body>
<main class="dieline">

  <!-- left side panel -->
  <section class="panel panel--side side-left">
    <div class="wordmark">Glimmo</div>
    <div class="tagline">Makes Every Smile Brightly Fresh!</div>
    <div class="info-box">
      <h3>Directions For Use</h3>
      <p>Directions for use is directed by physician and directed by a physician and directions for use.</p>
      <p>Directions for use is direct directed use Glimmo.</p>
    </div>
    <div class="batch">
      <div class="batch__row"><span>MFD :</span><div class="batch__field"></div></div>
      <div class="batch__row"><span>EXP :</span><div class="batch__field"></div></div>
      <div class="batch__row"><span>M.R.P :</span><div class="batch__field"></div></div>
    </div>
    <svg class="band" viewBox="0 0 130 110" preserveAspectRatio="none" aria-hidden="true">
      <path d="M0 40 Q65 20 130 30 L130 110 L0 110 Z" fill="var(--blue)"/>
      <path d="M0 52 Q65 34 130 44 L130 110 L0 110 Z" fill="var(--white)"/>
      <path d="M0 60 Q65 44 130 52 L130 110 L0 110 Z" fill="var(--green)"/>
    </svg>
  </section>

  <!-- front panel -->
  <section class="panel panel--face front">
    <div class="wave-art" role="img" aria-label="Flowing green line wave decoration"></div>
    <div class="product-art" role="img" aria-label="Glimmo plaque remover pick shown upright"></div>
    <div class="wordmark">Glimmo<span class="wordmark__dot"></span></div>
    <div class="tagline">Makes Every Smile Brightly Fresh!™</div>
    <div class="claim">Anatomically and Ergonomically correct</div>
    <div class="product-name">Dental Plaque Remover</div>
    <svg class="band" viewBox="0 0 340 110" preserveAspectRatio="none" aria-hidden="true">
      <path d="M0 50 Q170 -10 340 20 L340 110 L0 110 Z" fill="var(--blue)"/>
      <path d="M0 58 Q170 4 340 32 L340 110 L0 110 Z" fill="var(--white)"/>
      <path d="M0 66 Q170 16 340 42 L340 110 L0 110 Z" fill="var(--green)"/>
    </svg>
    <div class="count-badge">
      <span class="count-badge__label">Includes</span>
      <span class="count-badge__num">10</span>
      <span class="count-badge__unit">Pieces</span>
    </div>
    <svg class="seal" viewBox="0 0 110 100" aria-label="100% Satisfaction Guarantee">
      <circle cx="52" cy="46" r="40" fill="var(--blue)"/>
      <circle cx="52" cy="46" r="34" fill="none" stroke="var(--white)" stroke-width="1.5"/>
      <text x="52" y="38" text-anchor="middle" font-family="PT Sans" font-weight="700" font-size="20" fill="var(--white)">100%</text>
      <rect x="6" y="46" width="96" height="18" rx="2" fill="var(--green-light)"/>
      <text x="54" y="59" text-anchor="middle" font-family="PT Sans" font-size="13" fill="var(--white)">Satisfaction</text>
      <rect x="28" y="68" width="50" height="11" rx="2" fill="var(--green)"/>
      <text x="53" y="76.5" text-anchor="middle" font-family="PT Sans" font-weight="700" font-size="7" fill="var(--white)">GUARANTEE</text>
    </svg>
    <ul class="features">
      <li>REUSABLE</li>
      <li>EASY TO USE</li>
      <li>REMOVES PLAQUE QUICKLY</li>
    </ul>
  </section>

  <!-- right side panel -->
  <section class="panel panel--side side-right">
    <div class="wordmark">Glimmo</div>
    <div class="tagline">Makes Every Smile Brightly Fresh!</div>
    <div class="info-box">
      <h3>Introduction</h3>
      <div class="diagram" role="img" aria-label="Diagram of the Glimmo pick with labelled parts"></div>
      <div class="diagram-label" style="left:74px;top:40px;">Plaque<br>Remover<br>Tip</div>
      <div class="diagram-label" style="left:6px;top:120px;">Flexible<br>Body</div>
      <div class="diagram-label" style="left:6px;top:185px;">Easy to use<br>handle</div>
    </div>
    <svg class="band" viewBox="0 0 130 110" preserveAspectRatio="none" aria-hidden="true">
      <path d="M0 30 Q65 20 130 40 L130 110 L0 110 Z" fill="var(--blue)"/>
      <path d="M0 44 Q65 34 130 52 L130 110 L0 110 Z" fill="var(--white)"/>
      <path d="M0 52 Q65 44 130 60 L130 110 L0 110 Z" fill="var(--green)"/>
    </svg>
    <div class="marks" aria-hidden="true"><span></span><span></span><span></span></div>
  </section>

  <!-- back panel -->
  <section class="panel panel--face back">
    <div class="wordmark">Glimmo<span class="wordmark__dot"></span></div>
    <div class="tagline">Makes Every Smile Brightly Fresh!™</div>
    <div class="info-box">
      <p>Directions for use is directed by physician and directed by a physician and directions for use.</p>
      <p>Directions for use is direct directed use Glimmo.</p>
      <p>Rinse the tip before and after each use. Store dry in the box. Keep away from small children and heat.</p>
      <p>Replace when the tip shows wear.</p>
    </div>
    <svg class="band" viewBox="0 0 340 110" preserveAspectRatio="none" aria-hidden="true">
      <path d="M0 20 Q170 -10 340 50 L340 110 L0 110 Z" fill="var(--blue)"/>
      <path d="M0 32 Q170 4 340 58 L340 110 L0 110 Z" fill="var(--white)"/>
      <path d="M0 42 Q170 16 340 66 L340 110 L0 110 Z" fill="var(--green)"/>
    </svg>
  </section>

</main>
</body>
</html>
```